Business Card Design Project

We are looking for a new business card design for a Drilling company in WA, Australia.

We are in between offices, however require a design in the meantime due to some upcoming events with our basic information.

The Logo for our company is Blue and Grey and would like this colour scheme throughout.

We are quite a new company so would like a memorable design that stands out and communicates a strong commitment to safety, quality of work and performance.

The company name is Ironbark Boring Group (IBG)

The details to be included are as follows:

Gavin Thorley
Managing Director
m.0481639207
e.gavin@ibgpty.com.au

Martin Thorley
Director
m.0419852637
e.martin@ibgpty.com.au

Industry/Entity Type

Events

Requirements
Must have
• Under the Logo, we would like 'Western Australia'

```html
<!DOCTYPE html>
<html lang="en">
<head>
<meta charset="utf-8">
<title>Ironbark Boring Group — Business Cards</title>
<link rel="stylesheet" href="https://fonts.googleapis.com/css2?family=Archivo+Black&family=Oswald:wght@500&display=swap">
<style>
  :root {
    --canvas: #cccccc;
    --card: #ffffff;
    --brand-blue: #0b4a8f;
    --brand-grey: #7d7d80;
    --band-light: #efeff1;
    --band-mid: #d2d2d5;
    --band-dark: #9c9ca0;
  }
  * { margin: 0; padding: 0; box-sizing: border-box; }
  html, body { width: 1200px; height: 695px; overflow: hidden; }
  body { background: var(--canvas); position: relative; }

  .card {
    position: absolute;
    width: 505px;
    height: 289px;
    background: var(--card);
    overflow: hidden;
  }
  .card--front.row-1 { left: 98px; top: 40px; }
  .card--back.row-1  { left: 643px; top: 40px; }
  .card--front.row-2 { left: 98px; top: 370px; }
  .card--back.row-2  { left: 643px; top: 370px; border-radius: 3px; }

  .texture-band { position: absolute; left: 0; width: 100%; }
  .texture-band--top {
    top: 0; height: 90px;
    background: linear-gradient(to bottom, var(--band-light) 0%, var(--band-mid) 55%, var(--band-dark) 100%);
  }
  .texture-band--bottom {
    top: 200px; height: 89px;
    background: linear-gradient(to bottom, var(--band-dark) 0%, var(--band-mid) 45%, var(--band-light) 100%);
  }
  .texture-band--middle {
    top: 90px; height: 110px;
    background: linear-gradient(to bottom, var(--band-dark) 0%, var(--band-light) 35%, var(--band-light) 65%, var(--band-dark) 100%);
  }

  .brand-lockup {
    position: absolute;
    top: 90px; left: 0; width: 100%; height: 110px;
    display: flex; flex-direction: column; align-items: center; justify-content: center;
  }
  .brand-name {
    font-family: "Archivo Black", sans-serif;
    color: var(--brand-blue);
    font-size: 29px;
    line-height: 1;
    letter-spacing: 0.2px;
    border-bottom: 5px solid var(--brand-blue);
    padding-bottom: 8px;
  }
  .brand-region {
    font-family: "Archivo Black", sans-serif;
    color: var(--brand-grey);
    font-size: 14px;
    letter-spacing: 0.6px;
    align-self: flex-end;
    margin-right: 125px;
    margin-top: 3px;
  }

  .person {
    position: absolute; top: 0; left: 0; width: 100%; height: 90px;
    text-align: center; padding-top: 12px;
  }
  .person-name {
    font-family: "Archivo Black", sans-serif;
    color: var(--brand-blue);
    font-size: 36px;
    line-height: 1.05;
    letter-spacing: 0.5px;
  }
  .person-role {
    font-family: "Archivo Black", sans-serif;
    color: var(--brand-grey);
    font-size: 17px;
    line-height: 1.3;
  }

  .contact {
    position: absolute; top: 200px; left: 0; width: 100%; height: 89px;
    text-align: center; padding-top: 18px;
    font-family: "Oswald", sans-serif;
    font-weight: 500;
    color: var(--brand-grey);
    font-size: 21px;
    line-height: 32px;
  }
</style>
</head>
<body>

  <section class="card card--front row-1">
    <div class="texture-band texture-band--top" role="img" aria-label="Fine circular lattice texture fading into grey"></div>
    <div class="brand-lockup">
      <span class="brand-name">Ironbark Boring Group</span>
      <span class="brand-region">Western Australia</span>
    </div>
    <div class="texture-band texture-band--bottom" role="img" aria-label="Fine circular lattice texture fading from grey"></div>
  </section>

  <section class="card card--back row-1">
    <div class="person">
      <h1 class="person-name">Gavin Thorley</h1>
      <p class="person-role">Managing Director</p>
    </div>
    <div class="texture-band texture-band--middle" role="img" aria-label="Fine circular lattice texture band with grey edges"></div>
    <div class="contact">
      <p class="contact-phone">0481639207</p>
      <p class="contact-email">gavin@ibgpty.com.au</p>
    </div>
  </section>

  <section class="card card--front row-2">
    <div class="texture-band texture-band--top" role="img" aria-label="Fine circular lattice texture fading into grey"></div>
    <div class="brand-lockup">
      <span class="brand-name">Ironbark Boring Group</span>
      <span class="brand-region">Western Australia</span>
    </div>
    <div class="texture-band texture-band--bottom" role="img" aria-label="Fine circular lattice texture fading from grey"></div>
  </section>

  <section class="card card--back row-2">
    <div class="person">
      <h1 class="person-name">Martin Thorley</h1>
      <p class="person-role">Director</p>
    </div>
    <div class="texture-band texture-band--middle" role="img" aria-label="Fine circular lattice texture band with grey edges"></div>
    <div class="contact">
      <p class="contact-phone">0419852637</p>
      <p class="contact-email">martin@ibgpty.com.au</p>
    </div>
  </section>

</body>
</html>
```